Birchway Lending Social Media Campaign

I need social media campaign banners. Facebook and Instagram.
I would like them to incorporate local photos, my photo and my logo. I have some sample files of previous campaigns and I have a color scheme associated with my brand. My business operates in St. John's Newfoundland.

Target Market(s)

Home Buyers, Home Owners

Industry/Entity Type

Mortgage Brokering

Logo Text

Birchway Lending

Logo styles of interest
Lettermark Logo
Font styles to use
Other font styles liked:
• Times New Roman, I'm open to suggestion

Colors
0054AA
0677BA
7BADD7
CADEEF
E8F1F8
EE7325
F08F49
F5BC92
FAE3D3
FDF4ED

Requirements
Must have
• My name, photo, contact info, slogan
Nice to have
• We can discuss slogans to use, I can provide some suggestions.

```html
<!DOCTYPE html>
<html lang="en">
<head>
<meta charset="utf-8">
<title>Birchway Lending – Social Banners</title>
<link href="https://fonts.googleapis.com/css2?family=Poppins:ital,wght@0,400;0,500;0,600;0,700;0,800;1,700;1,800&display=swap" rel="stylesheet">
<style>
  :root{
    --stage:#d5d5d5;
    --paper:#ffffff;
    --navy:#0b1a5c;
    --orange:#fb4200;
    --ink:#2a2a2a;
    --btn-top:#1a8fe6;
    --btn-bottom:#0a5fc4;
    --btn-edge:#4fc1ff;
    --sky:#bcd9e8;
    --rock:#7d8a5e;
    --stone:#6b6a5c;
    --sea:#17445a;
  }
  *{margin:0;padding:0;box-sizing:border-box}
  html,body{width:836px;height:1200px;overflow:hidden}
  body{background:var(--stage);font-family:"Poppins",Arial,sans-serif;position:relative}
  .banner{position:absolute;overflow:hidden;box-shadow:0 6px 14px rgba(0,0,0,.28)}
  .banner-square{left:117px;top:80px;width:602px;height:602px}
  .banner-wide{left:75px;top:734px;width:686px;height:343px}
  .artboard{position:absolute;left:0;top:0;transform-origin:0 0;transform:scale(.5573);background:var(--paper)}
  .banner-square .artboard{width:1080px;height:1080px}
  .banner-wide .artboard{width:1232px;height:616px}
  .shapes{position:absolute;left:0;top:0}
  .abs{position:absolute;white-space:nowrap;line-height:1}

  .brand{display:flex;align-items:center;gap:14px;color:var(--orange);font-weight:800;text-transform:uppercase}
  .brand-mark{background:var(--navy)}

  .orange{color:var(--orange)}
  .navy{color:var(--navy)}
  .heavy{font-weight:800}
  .regular{font-weight:500}
  .semi{font-weight:600}

  .rule{position:absolute;height:3px;background:var(--orange)}
  .rule::before{content:"";position:absolute;left:0;top:-2px;height:7px;width:136px;background:var(--orange);border-radius:4px}

  .lede{color:var(--ink);font-weight:500;line-height:1.22}
  .lede strong{color:var(--navy);font-weight:700}

  .agent{color:#fff;font-weight:700;text-transform:uppercase}
  .contact{display:flex;align-items:center;color:#fff;font-weight:500}
  .contact svg{flex:none;background:var(--navy);border-radius:8px}

  .cta{position:absolute;display:flex;align-items:center;justify-content:center;gap:8px;
       background:linear-gradient(var(--btn-top),var(--btn-bottom));border:3px solid var(--btn-edge);
       border-radius:12px;color:#fff;font-style:italic;font-weight:800;text-transform:uppercase}
</style>
</head>
<body>

<svg width="0" height="0" style="position:absolute">
  <defs>
    <linearGradient id="harbour" x1="0" y1="0" x2="0.35" y2="1">
      <stop offset="0" stop-color="#c9e2ef"/>
      <stop offset=".22" stop-color="#9ab3a0"/>
      <stop offset=".45" stop-color="#7d8a5e"/>
      <stop offset=".65" stop-color="#6b6a5c"/>
      <stop offset=".85" stop-color="#1f5468"/>
      <stop offset="1" stop-color="#123646"/>
    </linearGradient>
    <symbol id="icon-phone" viewBox="0 0 40 40">
      <path d="M13 9l4 5-2.5 3c1.5 3.5 4 6 7.5 7.5l3-2.5 5 4-2 4c-9 1-18-8-17-17z" fill="none" stroke="#fff" stroke-width="2.4" stroke-linejoin="round"/>
      <path d="M23 10a8 8 0 0 1 7 7M23 15a3 3 0 0 1 2 2" fill="none" stroke="#fff" stroke-width="2" stroke-linecap="round"/>
    </symbol>
    <symbol id="icon-mail" viewBox="0 0 40 40">
      <rect x="7" y="11" width="26" height="18" fill="none" stroke="#fff" stroke-width="2.4"/>
      <path d="M7 11l13 10 13-10M7 29l10-9M33 29l-10-9" fill="none" stroke="#fff" stroke-width="2"/>
    </symbol>
    <symbol id="icon-web" viewBox="0 0 40 40">
      <circle cx="20" cy="20" r="12" fill="none" stroke="#fff" stroke-width="2.4"/>
      <path d="M8 20h24M20 8c-6 7-6 17 0 24M20 8c6 7 6 17 0 24M10 14h20M10 26h20" fill="none" stroke="#fff" stroke-width="1.8"/>
    </symbol>
  </defs>
</svg>

<!-- Square post -->
<section class="banner banner-square">
  <div class="artboard">
    <svg class="shapes" width="1080" height="1080" viewBox="0 0 1080 1080">
      <polygon points="983,121 1054,121 1054,166 983,126" fill="var(--orange)"/>
      <polygon role="img" aria-label="Aerial photo of a St. John's harbour hillside with colourful houses along the water" points="582,278 817,141 1054,278 1054,846 582,846" fill="url(#harbour)"/>
      <polygon points="517,210 817,44 1080,195 1080,276 817,124 582,262 517,296" fill="var(--navy)"/>
      <polygon points="0,813 538,813 615,946 538,1080 0,1080" fill="var(--orange)"/>
      <polygon points="585,863 1080,863 1080,1031 585,1031 628,946" fill="var(--navy)"/>
      <g fill="#ffffff" opacity=".07">
        <polygon points="940,898 990,898 1040,946 990,994 940,994 990,946"/>
        <polygon points="1000,898 1050,898 1080,926 1080,966 1050,994 1000,994 1050,946"/>
      </g>
    </svg>

    <div class="abs brand" style="left:30px;top:168px;font-size:40px">
      <span class="brand-mark" style="width:34px;height:34px"></span>Birchway Lending
    </div>

    <div class="abs orange heavy" style="left:30px;top:262px;font-size:54px">UNLOCK</div>
    <div class="abs navy regular" style="left:30px;top:318px;font-size:52px">THE DOOR TO</div>
    <div class="abs orange heavy" style="left:28px;top:372px;font-size:76px">YOUR</div>
    <div class="abs orange heavy" style="left:28px;top:444px;font-size:76px;letter-spacing:-1px">DREAM HOME</div>
    <div class="abs navy semi" style="left:28px;top:516px;font-size:76px">WITH US</div>
    <div class="rule" style="left:30px;top:615px;width:525px"></div>

    <p class="abs lede" style="left:28px;top:650px;font-size:34px">
      Let Us Help You Unlock Your<br><strong>DREAM HOME TODAY</strong><br>With Low Rates &amp; Great Deals!
    </p>

    <div class="abs agent" style="left:28px;top:842px;font-size:36px">Maren Holloway</div>
    <div class="abs contact" style="left:30px;top:894px;font-size:30px;gap:14px">
      <svg width="42" height="42"><use href="#icon-phone"/></svg>709-555-0142
    </div>
    <div class="abs contact" style="left:30px;top:945px;font-size:30px;gap:14px">
      <svg width="42" height="42"><use href="#icon-mail"/></svg>hello@birchwaylending.com
    </div>
    <div class="abs contact" style="left:30px;top:996px;font-size:30px;gap:14px">
      <svg width="42" height="42"><use href="#icon-web"/></svg>www.birchwaylending.com
    </div>

    <div class="cta" style="left:660px;top:908px;width:278px;height:78px;font-size:30px">Get Started
      <svg width="38" height="28" viewBox="0 0 38 28"><path d="M3 3l11 11-11 11M19 3l11 11-11 11" fill="none" stroke="#fff" stroke-width="6"/></svg>
    </div>
  </div>
</section>

<!-- Wide post -->
<section class="banner banner-wide">
  <div class="artboard">
    <svg class="shapes" width="1232" height="616" viewBox="0 0 1232 616">
      <polygon points="1112,86 1183,86 1183,128 1112,90" fill="var(--orange)"/>
      <polygon role="img" aria-label="Aerial photo of a St. John's harbour hillside with colourful houses along the water" points="721,208 951,86 1183,208 1183,444 721,444" fill="url(#harbour)"/>
      <polygon points="659,177 951,10 1232,172 1232,236 951,70 721,205 659,237" fill="var(--navy)"/>
      <polygon points="0,452 724,452 776,534 724,616 0,616" fill="var(--orange)"/>
      <polygon points="734,452 1232,452 1232,616 734,616 786,534" fill="var(--navy)"/>
      <g fill="#ffffff" opacity=".07">
        <polygon points="1050,470 1110,470 1170,534 1110,598 1050,598 1110,534"/>
        <polygon points="1125,470 1185,470 1232,520 1232,548 1185,598 1125,598 1185,534"/>
      </g>
    </svg>

    <div class="abs brand" style="left:52px;top:70px;font-size:34px">
      <span class="brand-mark" style="width:30px;height:30px"></span>Birchway Lending
    </div>

    <div class="abs navy" style="left:46px;top:160px;font-size:38px;font-weight:600">UNLOCK THE DOOR TO YOUR</div>
    <div class="abs orange heavy" style="left:44px;top:198px;font-size:74px;letter-spacing:-1px">DREAM HOME</div>
    <div class="abs navy semi" style="left:44px;top:270px;font-size:74px">WITH US</div>
    <div class="rule" style="left:46px;top:351px;width:535px"></div>

    <p class="abs lede" style="left:44px;top:370px;font-size:26px;line-height:1.18">
      Let Us Help You Unlock Your <strong>DREAM HOME TODAY</strong><br>With Low Rates &amp; Great Deals!
    </p>

    <div class="abs agent" style="left:46px;top:464px;font-size:28px">Maren Holloway</div>
    <div class="abs contact" style="left:48px;top:503px;font-size:26px;gap:10px">
      <svg width="32" height="32"><use href="#icon-phone"/></svg>709-555-0142
      <svg width="32" height="32" style="margin-left:18px"><use href="#icon-mail"/></svg>hello@birchwaylending.com
    </div>
    <div class="abs contact" style="left:48px;top:540px;font-size:26px;gap:10px">
      <svg width="32" height="32"><use href="#icon-web"/></svg>www.birchwaylending.com
    </div>

    <div class="cta" style="left:814px;top:502px;width:240px;height:66px;font-size:26px">Get Started
      <svg width="32" height="24" viewBox="0 0 38 28"><path d="M3 3l11 11-11 11M19 3l11 11-11 11" fill="none" stroke="#fff" stroke-width="6"/></svg>
    </div>
  </div>
</section>

</body>
</html>
```